Communication of Recommended Belief Letter

To Whom This May Concern,

My company's name is Brookfane LLC. I would like to send electronic messages to my clients. Therefore, I would like PixelForge to create a letterhead template to say Brookfane- without the LLC. My messages could extend up to 20 pages long. I would like something that is chic, fancy, and has creative designs. The background color should be white. The creative designs are open for suggestions without color restrictions. Font type and color are also open for suggestions. It may be what you believe best suite's the letterhead. I would like the letterhead to include the company logo. Please see attachment for file. Thank you.

Target Market(s)

working class American's

Industry/Entity Type

Communication

Contact Information for Business Card

The business card should be chic and fancy.

Font styles to use
Script

Requirements
Must have
• Company name: Brookfane LLC
• Company symbol: Please see attachment
• Name: Moriel Haskins
• Title: President
• Company website: www.brookfanellc-example.com
Nice to have
• Open for suggestions

```html
<!DOCTYPE html>
<html lang="en">
<head>
<meta charset="utf-8">
<title>Brookfane Business Card</title>
<link rel="stylesheet" href="https://fonts.googleapis.com/css2?family=Cinzel:wght@400&family=PT+Sans:wght@400;700&display=swap">
<style>
  :root {
    --stage: #000000;
    --card-front: #f2f2f2;
    --gold-deep: #a0650a;
    --gold-mid: #c9a21a;
    --gold-light: #ddd23a;
    --gold-text: #9a6a0c;
    --gold-name: #b88f10;
    --ink: #2a2a2a;
    --white: #ffffff;
  }
  * { margin: 0; padding: 0; box-sizing: border-box; }
  html, body {
    width: 1200px; height: 900px; overflow: hidden;
    background: var(--stage);
  }
  .stage { position: relative; width: 1200px; height: 900px; }

  .card {
    position: absolute; top: 200px; width: 310px; height: 502px;
  }
  .card-front {
    left: 265px;
    background: var(--card-front);
    border-radius: 56px 0 56px 0;
  }
  .card-back {
    left: 641px; width: 309px;
    border-radius: 0 56px 0 56px;
    background: radial-gradient(ellipse 75% 60% at 50% 42%, var(--gold-light) 0%, var(--gold-mid) 55%, var(--gold-deep) 100%);
  }

  .brand {
    position: absolute; left: 0; right: 0; text-align: center;
    font-family: "Cinzel", serif; font-weight: 400;
    font-size: 40px; letter-spacing: 0.5px; line-height: 1;
  }
  .card-front .brand { top: 152px; color: var(--gold-text); }
  .card-back .brand { top: 398px; color: var(--white); }

  .brand-dot {
    position: absolute; left: 50%; top: 52px;
    width: 52px; height: 52px; margin-left: -26px;
    border-radius: 50%;
    background: var(--gold-mid);
  }

  .contact {
    position: absolute; left: 36px; top: 282px;
    font-family: "PT Sans", sans-serif; color: var(--ink);
    font-size: 13.5px; line-height: 21px;
  }
  .person-name {
    font-weight: 700; font-size: 17.5px; color: var(--gold-name);
    line-height: 22px;
  }
  .person-title { margin-bottom: 22px; }
  .address { margin-bottom: 21px; }
  .channel { display: flex; align-items: center; gap: 7px; }
  .channel svg { width: 11px; height: 11px; flex: none; }
</style>
</head>
<body>
<main class="stage">
  <section class="card card-front">
    <div class="brand-dot"></div>
    <div class="brand">Brookfane</div>
    <div class="contact">
      <p class="person-name">Moriel Haskins</p>
      <p class="person-title">President</p>
      <p class="address">P.O. Box 2710, Alder<br>Ridge, Vermont 05341</p>
      <p class="channel">
        <svg viewBox="0 0 12 12" aria-hidden="true"><path fill="#b88f10" d="M2.5 1l2 2.2-1 1.3c.7 1.5 1.8 2.6 3.2 3.3l1.3-1 2.2 2-1.2 1.7C5 10 1.6 6.6 1 2.3z"/></svg>
        555 014 2387
      </p>
      <p class="channel">
        <svg viewBox="0 0 12 12" aria-hidden="true"><rect x="1" y="2.5" width="10" height="7" fill="#b88f10"/><path d="M1 2.5l5 4 5-4" fill="none" stroke="#f2f2f2" stroke-width="1"/></svg>
        info@brookfanellc-example.com
      </p>
      <p class="channel">
        <svg viewBox="0 0 12 12" aria-hidden="true"><circle cx="6" cy="6" r="5" fill="#b88f10"/><path d="M1 6h10M6 1c-2 2.5-2 7.5 0 10M6 1c2 2.5 2 7.5 0 10" fill="none" stroke="#f2f2f2" stroke-width="0.8"/></svg>
        www.brookfanellc-example.com
      </p>
    </div>
  </section>

  <section class="card card-back">
    <div class="brand">Brookfane</div>
  </section>
</main>
</body>
</html>
```